Luxury Business Card Design for High-End Window Treatments

Gilded Slatworks
Custom Plantation Shutters & Architectural Shading Systems

⸻

BACK

Daniel Ferrowitz
Owner

Custom Interior & Exterior Window Treatments

919-555-0187
gildedslatworks.example

I have included a picture that I’m hoping we can use on the back, but I’m also wondering if you can get rid of the ladder? Should we get rid of shutters , shades and blinds underneath Gilded Slatworks?

Target Market(s)

High-end residential homeowners, custom home builders, architects, interior designers, and luxury renovation clients seeking premium plantation shutters and motorized architectural shading systems.

Industry/Entity Type

Custom Window treatments

Contact Information for Business Card

Front Gilded Slatworks Custom Plantation Shutters Motorized Architectural Shading Systems BACK Daniel Ferrowitz Owner 919-555-0187 GildedSlatworks.example Custom Interior & Exterior Window Treatments By Appointment

Requirements
Nice to have
• Not 100% sure on nice to halves or the color but you can definitely check out my website to get a better understanding of what I’m trying to do

```html
<!DOCTYPE html>
<html lang="en">
<head>
<meta charset="utf-8">
<title>Gilded Slatworks – Business Cards</title>
<link href="https://fonts.googleapis.com/css2?family=Libre+Bodoni:wght@600&family=Raleway:wght@400;500&family=Marcellus&display=swap" rel="stylesheet">
<style>
  :root {
    --backdrop: #e9e8ea;
    --card-dark: #1a1a1a;
    --photo-top: #262624;
    --photo-bottom: #141414;
    --gold: #bba963;
    --gold-bright: #f0d36a;
    --name-gold: #c3ae66;
    --cream: #efe9dc;
    --ink: #0c0c0c;
  }
  * { margin: 0; padding: 0; box-sizing: border-box; }
  html, body { width: 1200px; height: 1108px; overflow: hidden; background: var(--backdrop); }
  .canvas { position: relative; width: 1200px; height: 1108px; }
  .card { position: absolute; overflow: hidden; background: var(--card-dark); }
  .card--front { left: 219px; top: 50px; width: 774px; height: 473px; }
  .card--back  { left: 217px; top: 568px; width: 777px; height: 457px; }
  .photo {
    position: absolute; inset: 0;
    background: linear-gradient(180deg, var(--photo-top) 0%, #1d1d1c 55%, var(--photo-bottom) 100%);
  }
  .wave { position: absolute; left: 0; bottom: 0; width: 100%; height: 100%; }

  .contact { position: absolute; left: 38px; top: 56px; font-family: "Raleway", sans-serif; color: var(--cream); }
  .contact__name { font-family: "Libre Bodoni", serif; font-weight: 600; font-size: 29px; color: var(--name-gold); line-height: 1; }
  .contact__role { font-size: 17px; margin-top: 4px; }
  .contact__service { font-size: 17px; line-height: 22px; margin-top: 38px; margin-left: 2px; }
  .contact__lines { list-style: none; margin-top: 43px; font-size: 18px; }
  .contact__lines li { display: flex; align-items: center; gap: 10px; height: 29px; }
  .contact__lines svg { width: 18px; height: 18px; fill: var(--cream); }
  .contact__note { color: var(--gold-bright); opacity: .85; font-size: 18px; margin-top: 8px; }

  .brand { position: absolute; text-align: center; }
  .card--front .brand { left: 395px; top: 150px; width: 340px; }
  .card--back .brand { left: 170px; top: 118px; width: 400px; }
  .brand__name {
    font-family: "Raleway", sans-serif; font-weight: 400; color: var(--cream);
    line-height: 1.05;
  }
  .card--front .brand__name { font-size: 52px; }
  .card--back .brand__name { font-size: 64px; }
  .brand__tagline {
    font-family: "Marcellus", serif; color: var(--gold-bright);
    display: flex; justify-content: space-between; margin-top: 10px;
  }
  .card--front .brand__tagline { font-size: 27px; }
  .card--back .brand__tagline { font-size: 31px; margin-top: 14px; }
</style>
</head>
<body>
<main class="canvas">

  <section class="card card--front">
    <div class="photo" role="img" aria-label="Darkened photograph of a two-storey house with a covered porch and windows"></div>
    <svg class="wave" viewBox="0 0 774 473" preserveAspectRatio="none" aria-hidden="true">
      <path d="M0,400 C160,368 320,392 470,425 C610,455 710,455 774,378 L774,473 L0,473 Z" fill="var(--gold)"/>
      <path d="M0,392 C170,360 330,385 480,425 C620,462 720,470 774,425" fill="none" stroke="var(--ink)" stroke-width="6"/>
    </svg>

    <div class="contact">
      <h1 class="contact__name">Daniel Ferrowitz</h1>
      <p class="contact__role">Owner</p>
      <p class="contact__service">Custom Interior &amp; Exterior<br>Window Treatments</p>
      <ul class="contact__lines">
        <li>
          <svg viewBox="0 0 24 24" aria-hidden="true"><path d="M3 9c0-2 2-4 9-4s9 2 9 4v2h-5V9H8v2H3z"/><path d="M6 12h12l2 8H4z"/></svg>
          919-555-0187
        </li>
        <li>
          <svg viewBox="0 0 24 24" aria-hidden="true"><circle cx="12" cy="13" r="9"/></svg>
          GildedSlatworks.example
        </li>
      </ul>
      <p class="contact__note">By Appointment</p>
    </div>

    <div class="brand">
      <p class="brand__name">Gilded<br>Slatworks</p>
      <p class="brand__tagline"><span>Shutters</span><span>Shades</span><span>Blinds</span></p>
    </div>
  </section>

  <section class="card card--back">
    <div class="photo" role="img" aria-label="Darkened photograph of a house front with porch, windows and garden chairs"></div>
    <div class="brand">
      <p class="brand__name">Gilded<br>Slatworks</p>
      <p class="brand__tagline"><span>Shutters</span><span>Shades</span><span>Blinds</span></p>
    </div>
  </section>

</main>
</body>
</html>
```